Korvane Development and Management Corp. Business Card

A logo design project has been started for our Calgary-Alberta, Canada based land development and project management company. Using this logo, a clean, sleek, professional business card is to be developed (for digital or print media) representing the principals of the company (community, sustainability, and harmony).
Updates

Reason: Logo design recently completed.

Adobe Illustrator Vector file uploaded. Thanks, Lev

Target Market(s)

Similar business development professionals and other engineering project management personnel involved in land developemtn. Also used to as as the brand and image with both private individuals (Landowners), public officials (policy makers), and investors (banks, venture capitalists).

Industry/Entity Type

Digital

Requirements
Must have
• Open to designers opinion. Based on logo. Must have logo, and space for employee name, title, address, website, office / cell numbers.
Should not have
• No Palm trees or tropical references. Company is based in Calgary, Alberta, Canada.

```html
<!DOCTYPE html>
<html lang="en">
<head>
<meta charset="utf-8">
<title>Korvane Development and Management Corp. – Business Card</title>
<link rel="stylesheet" href="https://fonts.googleapis.com/css2?family=Open+Sans:wght@400;600&display=swap">
<style>
  :root {
    --backdrop: #6b4a34;
    --card: #23272e;
    --accent: #a4c639;
    --text-grey: #a5a9af;
    --shadow: rgba(0, 0, 0, 0.45);
  }
  html, body {
    margin: 0;
    padding: 0;
    width: 1200px;
    height: 1000px;
    overflow: hidden;
    background: var(--backdrop);
    font-family: "Open Sans", sans-serif;
  }
  .canvas {
    position: relative;
    width: 1200px;
    height: 1000px;
  }
  .card {
    position: absolute;
    left: 265px;
    width: 667px;
    height: 397px;
    background: var(--card);
    box-shadow: 0 4px 14px var(--shadow);
    overflow: hidden;
  }
  .card--front { top: 73px; }
  .card--back { top: 532px; }

  .brand {
    position: absolute;
    display: flex;
    align-items: center;
    color: var(--accent);
    font-weight: 400;
  }
  .brand__mark {
    background: var(--accent);
    flex: none;
  }
  .brand__name {
    display: flex;
    flex-direction: column;
    line-height: 1;
  }
  .brand__title {
    text-transform: uppercase;
    letter-spacing: 2px;
  }

  .card--front .brand {
    left: 86px;
    top: 148px;
    gap: 22px;
  }
  .card--front .brand__mark { width: 100px; height: 100px; }
  .card--front .brand__title { font-size: 56px; }
  .card--front .brand__tag { font-size: 20px; margin-top: 12px; }

  .card--back .brand {
    right: 22px;
    top: 46px;
    gap: 14px;
  }
  .card--back .brand__mark { width: 62px; height: 62px; }
  .card--back .brand__title { font-size: 36px; }
  .card--back .brand__tag { font-size: 13.5px; margin-top: 7px; }

  .person {
    position: absolute;
    left: 23px;
    top: 136px;
  }
  .person__name {
    margin: 0;
    font-size: 20px;
    font-weight: 600;
    color: var(--text-grey);
    letter-spacing: 0.5px;
    text-transform: uppercase;
    line-height: 1.1;
  }
  .person__role {
    margin: 1px 0 0;
    font-size: 15px;
    color: var(--accent);
  }

  .contact {
    position: absolute;
    left: 23px;
    top: 204px;
    list-style: none;
    margin: 0;
    padding: 0;
    color: var(--text-grey);
    font-size: 16px;
    line-height: 24px;
  }
  .contact__item {
    display: flex;
    align-items: flex-start;
    gap: 6px;
  }
  .contact__item + .contact__item { margin-top: 1px; }
  .contact__item--gap { margin-top: 17px !important; }
  .contact__icon {
    width: 12px;
    height: 12px;
    margin-top: 6px;
    flex: none;
    fill: var(--accent);
  }

  .baseband {
    position: absolute;
    left: 0;
    bottom: 2px;
    width: 100%;
    height: 11px;
    background: var(--accent);
  }
</style>
</head>
<body>
<main class="canvas">

  <section class="card card--front" aria-label="Business card front">
    <div class="brand">
      <span class="brand__mark"></span>
      <span class="brand__name">
        <span class="brand__title">Korvane</span>
        <span class="brand__tag">Development and Management Corp.</span>
      </span>
    </div>
  </section>

  <section class="card card--back" aria-label="Business card back">
    <div class="brand">
      <span class="brand__mark"></span>
      <span class="brand__name">
        <span class="brand__title">Korvane</span>
        <span class="brand__tag">Development and Management Corp.</span>
      </span>
    </div>

    <div class="person">
      <h1 class="person__name">Elliot Marwick</h1>
      <p class="person__role">Director</p>
    </div>

    <ul class="contact">
      <li class="contact__item">
        <svg class="contact__icon" viewBox="0 0 12 12" aria-hidden="true"><path d="M6 0a4.2 4.2 0 0 0-4.2 4.2C1.8 7.4 6 12 6 12s4.2-4.6 4.2-7.8A4.2 4.2 0 0 0 6 0zm0 6a1.8 1.8 0 1 1 0-3.6A1.8 1.8 0 0 1 6 6z"/></svg>
        <span>14 Ridgeline Court<br>Calgary AB T2P 4K9</span>
      </li>
      <li class="contact__item contact__item--gap">
        <svg class="contact__icon" viewBox="0 0 12 12" aria-hidden="true"><path d="M3 0h6a1 1 0 0 1 1 1v10a1 1 0 0 1-1 1H3a1 1 0 0 1-1-1V1a1 1 0 0 1 1-1zm0.8 1.2v8.4h4.4V1.2z"/></svg>
        <span>+1 403 555 0182</span>
      </li>
      <li class="contact__item">
        <svg class="contact__icon" viewBox="0 0 12 12" aria-hidden="true"><path d="M1 4.5C1 2.5 3.5 1.5 6 1.5s5 1 5 3v1H8.5V4.3H3.5v1.2H1zM2.5 6.5h7L11 11H1z"/></svg>
        <span>+1 403 555 0147</span>
      </li>
      <li class="contact__item contact__item--gap">
        <svg class="contact__icon" viewBox="0 0 12 12" aria-hidden="true"><path d="M6 0a6 6 0 1 0 0 12A6 6 0 0 0 6 0zm4.7 5.3H8.6a9 9 0 0 0-.8-3.8 4.8 4.8 0 0 1 2.9 3.8zM6 1.2c.6.8 1.3 2.2 1.4 4.1H4.6C4.7 3.4 5.4 2 6 1.2zM4.2 1.5a9 9 0 0 0-.8 3.8H1.3a4.8 4.8 0 0 1 2.9-3.8zM1.3 6.7h2.1a9 9 0 0 0 .8 3.8 4.8 4.8 0 0 1-2.9-3.8zM6 10.8c-.6-.8-1.3-2.2-1.4-4.1h2.8c-.1 1.9-.8 3.3-1.4 4.1zm1.8-.3a9 9 0 0 0 .8-3.8h2.1a4.8 4.8 0 0 1-2.9 3.8z"/></svg>
        <span>www.korvane-dev.com</span>
      </li>
    </ul>

    <div class="baseband"></div>
  </section>

</main>
</body>
</html>
```